Interactive Banner for Maplecrest Elementary School

title :"The Season of Stride”
Slogan: Khao, Khelo, Badho
(Eat, Play, Grow)

Students will place pictures of themselves doing their favorite sport or physical activity so will need space for 200 students.

Banner is around 128 sq feet. Will get exact dimensions.

Banner dimensions Length: 14 ft 9 in Height: 6 ft 9in

The border can be international flags, athletic symbols, etc..

Maybe use watermark athletic symbols in the background

incorporate logo

Target Market(s)

School community and mostly students to bring awareness to a healthy lifestyle

Industry/Entity Type

School

Font styles to use
Serif
Sans Serif

Requirements
Must have
• Space for photograph of children
• "The Season of Stride”
• Khao, Khelo, Badho
• (Eat, Play, Grow)
• Use our color palate listed. see below.
Nice to have
• international flag border

```html
<!DOCTYPE html>
<html lang="en">
<head>
<meta charset="utf-8">
<title>The Season of Stride – Maplecrest Elementary School</title>
<link rel="stylesheet" href="https://fonts.googleapis.com/css2?family=Arimo:wght@400;700&display=swap">
<style>
  :root {
    --paper: #ffffff;
    --frame-green: #00a14b;
    --frame-orange: #f15a24;
    --title-orange: #f15a24;
    --slogan-green: #00a14b;
    --crest-green: #1f5b3f;
    --runner-grey: #c9c9c9;
    --slot-line: rgba(255, 255, 255, 0.85);
  }
  * { box-sizing: border-box; margin: 0; padding: 0; }
  html, body {
    width: 1200px;
    height: 600px;
    overflow: hidden;
    background: var(--paper);
  }
  .banner {
    position: relative;
    width: 1200px;
    height: 600px;
    background: var(--paper);
    border: 8px solid var(--frame-green);
    font-family: "Arimo", Arial, sans-serif;
  }
  .banner__inner-frame {
    position: absolute;
    inset: 6px;
    border: 10px solid var(--frame-orange);
  }
  .headline {
    position: absolute;
    left: 60px;
    top: 84px;
    width: 740px;
    text-align: center;
    color: var(--title-orange);
    font-weight: 700;
  }
  .headline__lead {
    display: block;
    font-size: 66px;
    line-height: 1;
    letter-spacing: -0.5px;
  }
  .headline__main {
    display: block;
    font-size: 140px;
    line-height: 1;
    letter-spacing: -2px;
    margin-top: 2px;
  }
  .slogan {
    position: absolute;
    left: 60px;
    top: 300px;
    width: 740px;
    text-align: center;
    color: var(--slogan-green);
    font-weight: 700;
  }
  .slogan__words {
    display: block;
    font-size: 48px;
    line-height: 1;
  }
  .slogan__translation {
    display: block;
    margin-top: 6px;
    font-size: 24px;
    line-height: 1;
    font-weight: 400;
  }
  .school-mark {
    position: absolute;
    left: 870px;
    top: 100px;
    width: 280px;
    height: 230px;
    display: flex;
    flex-direction: column;
    align-items: center;
    justify-content: center;
    gap: 16px;
    text-align: center;
  }
  .school-mark__dot {
    width: 70px;
    height: 70px;
    border-radius: 50%;
    background: var(--crest-green);
  }
  .school-mark__name {
    color: var(--crest-green);
    font-size: 26px;
    font-weight: 700;
    line-height: 1.15;
    letter-spacing: 0.5px;
    text-transform: uppercase;
  }
  /* Runner strip doubling as the wall of 200 student photo slots (40 × 5) */
  .photo-wall {
    position: absolute;
    left: 80px;
    top: 398px;
    width: 1040px;
    height: 160px;
    border-radius: 6px;
    background:
      repeating-linear-gradient(90deg, transparent 0 24px, var(--slot-line) 24px 26px),
      repeating-linear-gradient(180deg, transparent 0 30px, var(--slot-line) 30px 32px),
      linear-gradient(180deg, #d2d2d2 0%, var(--runner-grey) 100%);
  }
</style>
</head>
<body>
  <main class="banner">
    <div class="banner__inner-frame"></div>

    <h1 class="headline">
      <span class="headline__lead">The Season of</span>
      <span class="headline__main">Stride</span>
    </h1>

    <p class="slogan">
      <span class="slogan__words">Khao, Khelo, Badho</span>
      <span class="slogan__translation">(Eat, Play, Grow)</span>
    </p>

    <div class="school-mark">
      <span class="school-mark__dot"></span>
      <span class="school-mark__name">Maplecrest<br>Elementary School</span>
    </div>

    <div class="photo-wall" role="img" aria-label="A row of grey silhouettes of children running to the right, laid over a grid of 200 slots for student photos"></div>
  </main>
</body>
</html>
```